" A RB DELTORA fornece soluções personalizadas para a geração de energia fotovoltaica, que é uma fonte sustentável proveniente de recursos limpos, sem emissão de carbono. Somos habilitados a importar e comercializar módulos fotovoltaicos que transformam a radiação solar em energia elétrica através de inversores. Temos equipe qualificada para instalar os equipamentos, atendendo todos os requisitos de segurança exigidos por lei. Os equipamentos têm certificação do Normaq, CE (Conformidade Européia) e OKP (Órgão de Perícia Industrial da Alemanha). "

```html
<!DOCTYPE html>
<html lang="pt-BR">
<head>
<meta charset="UTF-8">
<title>RB DELTORA — Cartões de visita</title>
<link rel="stylesheet" href="https://fonts.googleapis.com/css2?family=Montserrat:wght@400;600;700&display=swap">
<style>
  :root {
    --page-bg: #ecebe8;
    --navy: #16264a;
    --charcoal: #2b2621;
    --green: #58b23f;
    --green-light: #86cf62;
    --white: #ffffff;
    --logo-ink: #3a3a3a;
    --tagline-ink: #6b6b6b;
  }
  * { box-sizing: border-box; margin: 0; padding: 0; }
  html, body {
    width: 1200px;
    height: 1200px;
    overflow: hidden;
    background: var(--page-bg);
    font-family: "Montserrat", sans-serif;
  }
  .card-stack {
    position: absolute;
    left: 120px;
    top: 304px;
    display: flex;
    flex-direction: column;
    gap: 60px;
  }
  .business-card {
    position: relative;
    width: 960px;
    height: 266px;
    overflow: hidden;
    box-shadow: 0 6px 18px rgba(0, 0, 0, 0.18);
  }
  .business-card--navy { background: var(--navy); }
  .business-card--charcoal { background: var(--charcoal); }
  .card-swoosh {
    position: absolute;
    inset: 0;
    width: 100%;
    height: 100%;
  }
  .logo-tab {
    position: absolute;
    left: 34px;
    top: 0;
    width: 300px;
    height: 96px;
    background: var(--white);
    border-radius: 0 0 18px 18px;
    padding: 18px 22px 0;
  }
  .brand-row {
    display: flex;
    align-items: center;
    gap: 10px;
  }
  .brand-square {
    width: 26px;
    height: 26px;
    background: var(--green);
  }
  .brand-name {
    font-weight: 600;
    font-size: 30px;
    letter-spacing: 1px;
    color: var(--logo-ink);
    line-height: 1;
  }
  .brand-tagline {
    margin-top: 10px;
    font-size: 11px;
    color: var(--tagline-ink);
    white-space: nowrap;
  }
  .contact-list {
    position: absolute;
    right: 30px;
    top: 30px;
    list-style: none;
    display: flex;
    flex-direction: column;
    gap: 12px;
  }
  .contact-item {
    display: flex;
    align-items: center;
    justify-content: flex-end;
    gap: 14px;
    color: var(--white);
    font-size: 12px;
    font-weight: 600;
    letter-spacing: 0.3px;
  }
  .contact-icon {
    width: 16px;
    height: 16px;
    fill: var(--white);
  }
</style>
</head>
<body>
  <main class="card-stack">

    <article class="business-card business-card--navy">
      <svg class="card-swoosh" viewBox="0 0 960 266" preserveAspectRatio="none" aria-hidden="true">
        <path d="M0,188 C300,170 620,238 960,222 L960,266 L0,266 Z" fill="var(--green)"/>
        <path d="M0,212 C320,196 640,252 960,244 L960,266 L0,266 Z" fill="var(--navy)"/>
        <path d="M0,236 C340,224 660,262 960,256 L960,266 L0,266 Z" fill="var(--green-light)"/>
      </svg>
      <div class="logo-tab">
        <div class="brand-row">
          <span class="brand-square"></span>
          <span class="brand-name">RB DELTORA</span>
        </div>
        <p class="brand-tagline">Energia Solar Limpa para Casas e Empresas</p>
      </div>
      <ul class="contact-list">
        <li class="contact-item">(11) 90000-1234
          <svg class="contact-icon" viewBox="0 0 16 16"><path d="M3 1 L6 1 L7 5 L5 6.5 C6 8.5 7.5 10 9.5 11 L11 9 L15 10 L15 13 C15 14 14 15 13 15 C6.5 15 1 9.5 1 3 C1 2 2 1 3 1 Z"/></svg>
        </li>
        <li class="contact-item">(11) 95555-6789
          <svg class="contact-icon" viewBox="0 0 16 16"><path d="M4.5 0.5 H11.5 A1 1 0 0 1 12.5 1.5 V14.5 A1 1 0 0 1 11.5 15.5 H4.5 A1 1 0 0 1 3.5 14.5 V1.5 A1 1 0 0 1 4.5 0.5 Z M5 2.5 V12 H11 V2.5 Z M8 13 A0.8 0.8 0 1 0 8.01 13 Z"/></svg>
        </li>
        <li class="contact-item">CONTATO@RBDELTORA.COM.BR
          <svg class="contact-icon" viewBox="0 0 16 16"><path d="M1 3 H15 V13 H1 Z M2 4 L8 9 L14 4 Z"/></svg>
        </li>
        <li class="contact-item">WWW.RBDELTORA.COM.BR
          <svg class="contact-icon" viewBox="0 0 16 16"><path d="M2 2 H14 V11 H2 Z M3 3 V10 H13 V3 Z M6 12 H10 V13.5 H12 V15 H4 V13.5 H6 Z"/></svg>
        </li>
      </ul>
    </article>

    <article class="business-card business-card--charcoal">
      <svg class="card-swoosh" viewBox="0 0 960 266" preserveAspectRatio="none" aria-hidden="true">
        <path d="M0,188 C300,170 620,238 960,222 L960,266 L0,266 Z" fill="var(--green)"/>
        <path d="M0,212 C320,196 640,252 960,244 L960,266 L0,266 Z" fill="var(--charcoal)"/>
        <path d="M0,236 C340,224 660,262 960,256 L960,266 L0,266 Z" fill="var(--green-light)"/>
      </svg>
      <div class="logo-tab">
        <div class="brand-row">
          <span class="brand-square"></span>
          <span class="brand-name">RB DELTORA</span>
        </div>
        <p class="brand-tagline">Energia Solar Limpa para Casas e Empresas</p>
      </div>
      <ul class="contact-list">
        <li class="contact-item">(11) 90000-1234
          <svg class="contact-icon" viewBox="0 0 16 16"><path d="M3 1 L6 1 L7 5 L5 6.5 C6 8.5 7.5 10 9.5 11 L11 9 L15 10 L15 13 C15 14 14 15 13 15 C6.5 15 1 9.5 1 3 C1 2 2 1 3 1 Z"/></svg>
        </li>
        <li class="contact-item">(11) 95555-6789
          <svg class="contact-icon" viewBox="0 0 16 16"><path d="M4.5 0.5 H11.5 A1 1 0 0 1 12.5 1.5 V14.5 A1 1 0 0 1 11.5 15.5 H4.5 A1 1 0 0 1 3.5 14.5 V1.5 A1 1 0 0 1 4.5 0.5 Z M5 2.5 V12 H11 V2.5 Z M8 13 A0.8 0.8 0 1 0 8.01 13 Z"/></svg>
        </li>
        <li class="contact-item">CONTATO@RBDELTORA.COM.BR
          <svg class="contact-icon" viewBox="0 0 16 16"><path d="M1 3 H15 V13 H1 Z M2 4 L8 9 L14 4 Z"/></svg>
        </li>
        <li class="contact-item">WWW.RBDELTORA.COM.BR
          <svg class="contact-icon" viewBox="0 0 16 16"><path d="M2 2 H14 V11 H2 Z M3 3 V10 H13 V3 Z M6 12 H10 V13.5 H12 V15 H4 V13.5 H6 Z"/></svg>
        </li>
      </ul>
    </article>

  </main>
</body>
</html>
```